Webdesign für Birke Werkstatt
Zielgruppe
Birke Werkstatt produziert GfK Formteile und Abdeckungen
Einzelanfertigungen • Negativ - Formenbau • Prototyping • Ur-Modellbau
Formteile • Abdeckungen • Behälter • Sonderanfertigungen • Beschichtungen
Prototypen Modellbau • Anfertigung von Negativformen • Reparaturen • Fahrzeugteile
Hauptzielgruppe ist die Luftfahrtindustrie (Abdeckungen für Triebwerke)
Durch den Prototypenbau und die Einzelanfertigungen ist die Zielgruppe nicht klar zu definieren. Es werden Einzelteile jeglicher Art aus GfK hergestellt.
Dies können auch Anbauteile für PKW, Poolbeschichtungen, Teile für Boote etc sein.
Es gibt auch Kleinserien. Beispielsweise baut Birke-Werkstatt Motorhauben für Hallo-Brenner Rasenmähertrecker aus den 70er Jahren nach, die es nicht mehr zu kaufen gibt.
Aufgabenstellung
Der Designer hat alle Freiheiten. Die Seite muss natürlich responsiv funktionieren.
Außer dem Logo gibt es keine must-haves.
Schriftart aus dem Logo: EXO 2

```html
<!DOCTYPE html>
<html lang="de">
<head>
<meta charset="utf-8">
<title>Birke Werkstatt – GfK Formteile</title>
<link href="https://fonts.googleapis.com/css2?family=Exo+2:wght@300;400;500;700;800&display=swap" rel="stylesheet">
<style>
:root{
  --blue:#1a5b9a;
  --blue-dark:#124a80;
  --text:#1e1e1e;
  --grey-bg:#f1f1f1;
  --box-bg:#eeeeee;
  --orange:#f39200;
  --white:#ffffff;
}
*{margin:0;padding:0;box-sizing:border-box}
html,body{width:1200px;height:2729px;overflow:hidden}
body{position:relative;font-family:"Exo 2",sans-serif;color:var(--text);background:var(--white)}
.abs{position:absolute}

/* header */
.brand-mark{left:120px;top:40px;width:160px;height:160px;border-radius:50%;background:var(--blue)}
.brand-name{left:322px;top:70px;font-size:64px;font-weight:800;color:var(--blue);line-height:1;letter-spacing:-1px}
.brand-tagline{left:322px;top:143px;font-size:19px;color:#444}
.meta-links{top:18px;left:899px;font-size:15px;color:var(--blue)}
.meta-links span{margin-right:22px}
.flag{left:1055px;top:17px;width:35px;height:22px;box-shadow:0 1px 3px rgba(0,0,0,.4)}

.main-nav{left:0;top:180px;width:1200px;height:51px;background:var(--blue);display:flex;padding-left:303px}
.main-nav a{color:var(--white);text-decoration:none;font-size:16px;line-height:51px;padding:0 22px;position:relative;border-right:1px solid rgba(255,255,255,.12)}
.main-nav a.active{background:var(--blue-dark)}
.main-nav a.active::after{content:"";position:absolute;left:50%;bottom:-8px;margin-left:-8px;border:8px solid transparent;border-bottom:0;border-top-color:var(--blue-dark)}

/* hero */
.hero{left:0;top:231px;width:1200px;height:492px;background:linear-gradient(180deg,#b9d3df 0%,#d7e4ea 45%,#aab2b8 70%,#8f969b 100%)}
.hero-caption{left:808px;top:266px;width:392px;height:111px;background:rgba(255,255,255,.85);padding:18px 32px;font-size:31px;font-weight:800;color:var(--blue);line-height:1.17}
.slide-arrow{width:62px;height:62px;background:rgba(255,255,255,.8);display:flex;align-items:center;justify-content:center}

/* about */
.section-title{width:1200px;left:0;text-align:center;font-size:30px;font-weight:800;color:var(--blue)}
.about-photo{left:108px;top:837px;width:453px;height:333px;background:linear-gradient(135deg,#2f5fb5 0%,#3a6fc4 50%,#c9ccd0 100%)}
.about-text{left:108px;top:1188px;width:460px;font-size:19px;line-height:24px}
.feature{left:643px;width:447px;height:60px;background:var(--box-bg);display:flex;align-items:center;padding-left:10px;font-size:31px;font-weight:300;color:var(--blue)}
.feature svg{margin-right:14px}

/* products */
.products{left:0;top:1390px;width:1200px;height:870px;background:var(--grey-bg)}
.view-toggle{left:1008px;top:1455px}
.card{top:1530px;width:289px;height:503px;background:var(--white);box-shadow:0 2px 8px rgba(0,0,0,.12);text-align:center}
.card-photo{margin:12px;height:262px}
.card-title{font-size:20px;font-weight:800;color:var(--blue);line-height:24px;margin-top:24px;padding:0 14px;height:54px}
.card-text{font-size:16.5px;line-height:21px;padding:0 14px;margin-top:2px;height:90px}
.card-button{display:inline-block;width:102px;height:30px;line-height:30px;background:var(--orange);color:var(--white);font-weight:700;font-size:16px;box-shadow:0 4px 8px rgba(243,146,0,.35)}
.card-arrow{width:61px;height:61px;background:var(--white);display:flex;align-items:center;justify-content:center}

/* contact */
.contact-tab{left:89px;top:2218px;width:204px;height:43px;background:var(--blue);clip-path:polygon(18px 0,100% 0,100% 100%,0 100%);color:var(--white);font-size:30px;font-weight:800;padding-left:50px;line-height:44px}
.footer{left:0;top:2260px;width:1200px;height:469px;background:var(--blue);color:var(--white)}
.footer-name{left:137px;top:2296px;font-size:29px;font-weight:800;color:var(--white)}
.footer-address{left:137px;top:2348px;font-size:20px;font-weight:700;line-height:24px;color:var(--white)}
.footer-address .gap{height:24px}
.footer-address b{display:inline-block;width:60px;font-weight:700}
.form-title{left:661px;top:2298px;font-size:27px;font-weight:800;color:var(--white)}
.field{left:641px;width:447px;background:var(--white);border:2px solid #d9e2ec;color:var(--blue);font-size:19px;padding:8px 19px}
.send{left:969px;top:2627px;width:121px;height:38px;background:var(--blue-dark);color:var(--white);font-weight:800;font-size:19px;text-align:center;line-height:38px;letter-spacing:.5px}
</style>
</head>
<body>

<header>
  <div class="abs brand-mark" aria-hidden="true"></div>
  <div class="abs brand-name">Birke Werkstatt</div>
  <div class="abs brand-tagline">GfK Formteile | Ur-Modellbau | Prototyping</div>
  <div class="abs meta-links"><span>Impressum</span><span>AGB</span></div>
  <svg class="abs flag" viewBox="0 0 35 22" aria-label="Deutsch"><rect width="35" height="7.4" fill="#000"/><rect y="7.3" width="35" height="7.4" fill="#dd0000"/><rect y="14.6" width="35" height="7.4" fill="#ffce00"/></svg>
  <nav class="abs main-nav">
    <a class="active">Startseite</a><a>Über uns</a><a>Produkte &amp; Dienstleistungen</a><a>Kontakt</a>
  </nav>
</header>

<section>
  <div class="abs hero" role="img" aria-label="Foto: Großraum-Passagierflugzeug mit gelbem Flugzeugschlepper auf dem Vorfeld"></div>
  <div class="abs hero-caption">Abdeckungen für<br>Triebwerke</div>
  <div class="abs slide-arrow" style="left:0;top:452px"><svg width="22" height="32" viewBox="0 0 22 32"><path d="M17 3 5 16l12 13" fill="none" stroke="#1a5b9a" stroke-width="5"/></svg></div>
  <div class="abs slide-arrow" style="left:1138px;top:452px"><svg width="22" height="32" viewBox="0 0 22 32"><path d="M5 3l12 13L5 29" fill="none" stroke="#1a5b9a" stroke-width="5"/></svg></div>
</section>

<section>
  <h2 class="abs section-title" style="top:757px">Über uns</h2>
  <div class="abs about-photo" role="img" aria-label="Foto: Triebwerk unter blauer Schutzabdeckung auf Transportgestell"></div>
  <p class="abs about-text">Wir entwickeln und fertigen geometrisch an­spruchsvolle Formteile von höchster Qualität. Die von uns konzipierten Verbundwerkstoffe mit ihren herausragenden Oberflächen- und Materialeigen­schaften bieten konstruktive Vorteile und erweit­ern die gestalterischen Möglichkeiten.</p>
  <div class="abs feature" style="top:837px">
    <svg width="66" height="46" viewBox="0 0 66 46"><path d="M2 10h14l10-6 12 2 10-2h16v22H56L40 42c-3 2-6 1-7-1l-4 2c-3 1-5-1-6-3l-4 1c-3 0-5-2-5-4l-3-1c-3-1-3-4-1-6L2 24z" fill="#1a5b9a"/><path d="M26 14l12-4 14 16" fill="none" stroke="#eee" stroke-width="3"/></svg>
    Kundenorientiert
  </div>
  <div class="abs feature" style="top:911px">
    <svg width="66" height="46" viewBox="0 0 66 46"><path d="M6 42a27 27 0 0 1 54 0" fill="none" stroke="#1a5b9a" stroke-width="8"/><path d="M30 40l22-22" stroke="#1a5b9a" stroke-width="5"/><circle cx="30" cy="40" r="5" fill="#1a5b9a"/></svg>
    Leistungsstark
  </div>
</section>

<section>
  <div class="abs products"></div>
  <h2 class="abs section-title" style="top:1443px">Produkte &amp; Dienstleistungen</h2>
  <svg class="abs view-toggle" width="82" height="28" viewBox="0 0 82 28"><path d="M8 6 2 14l6 8M38 6l6 8-6 8" fill="none" stroke="#1a5b9a" stroke-width="3"/><rect x="15" y="4" width="8" height="20" fill="#1a5b9a"/><rect x="25" y="4" width="6" height="20" fill="#1a5b9a"/><g fill="#6b6b6b"><rect x="56" y="3" width="7" height="7"/><rect x="65" y="3" width="7" height="7"/><rect x="74" y="3" width="7" height="7"/><rect x="56" y="12" width="7" height="7"/><rect x="65" y="12" width="7" height="7"/><rect x="74" y="12" width="7" height="7"/><rect x="56" y="21" width="7" height="7"/><rect x="65" y="21" width="7" height="7"/><rect x="74" y="21" width="7" height="7"/></g></svg>

  <article class="abs card" style="left:108px">
    <div class="card-photo" role="img" aria-label="Foto: gelbe Triebwerksabdeckung an einem Flugzeugtriebwerk" style="background:linear-gradient(135deg,#e5e63a,#c9c92a 55%,#8a8f94)"></div>
    <h3 class="card-title">Luftfahrt Formbauteile</h3>
    <p class="card-text">Anfertigung von Triebwerkcover für jeden Triebwerktypen.</p>
    <span class="card-button">Details</span>
  </article>
  <article class="abs card" style="left:455px">
    <div class="card-photo" role="img" aria-label="Foto: große aufblasbare graue Sonderabdeckung in einer Werkhalle" style="background:linear-gradient(135deg,#c9ccd0,#a9aeb3 60%,#7d8287)"></div>
    <h3 class="card-title">Aufblasbare Sonderabdeckungen</h3>
    <p class="card-text">Anfertigung von Triebwerkcover für jeden Triebwerktypen.</p>
    <span class="card-button">Details</span>
  </article>
  <article class="abs card" style="left:800px">
    <div class="card-photo" role="img" aria-label="Foto: blaue technische Formbauteile mit gelbem Innenring" style="background:linear-gradient(135deg,#2a5cc8,#3569d6 60%,#b58a5a)"></div>
    <h3 class="card-title">Formbauteile</h3>
    <p class="card-text">Anfertigung von technischen Formbauteilen (Einzelstück oder Kleinserien).</p>
    <span class="card-button">Details</span>
  </article>

  <div class="abs card-arrow" style="left:22px;top:1742px"><svg width="22" height="32" viewBox="0 0 22 32"><path d="M17 3 5 16l12 13" fill="none" stroke="#1a5b9a" stroke-width="5"/></svg></div>
  <div class="abs card-arrow" style="left:1113px;top:1742px"><svg width="22" height="32" viewBox="0 0 22 32"><path d="M5 3l12 13L5 29" fill="none" stroke="#1a5b9a" stroke-width="5"/></svg></div>
</section>

<footer>
  <div class="abs contact-tab">Kontakt</div>
  <div class="abs footer"></div>
  <div class="abs footer-name">Birke Werkstatt</div>
  <div class="abs footer-address">
    Geschäftsführer: M. Halden<br>Lindenhofweg 14<br>31847 Elsdorf
    <div class="gap"></div>
    <b>Tel.</b>+49 000 / 123 45 67<br><b>Fax.</b>+49 000 / 123 45 68
  </div>
  <div class="abs form-title">Ihre Nachricht</div>
  <div class="abs field" style="top:2346px;height:43px">Name</div>
  <div class="abs field" style="top:2406px;height:43px">E-Mail</div>
  <div class="abs field" style="top:2467px;height:144px">Nachricht</div>
  <div class="abs send">SENDEN</div>
</footer>

</body>
</html>
```